Modellprojekt in der Jugendhilfe sucht für Abschlussbroschüre ansprechendes Design
Zielgruppe
Wir sind ein Jugendhilfeträger und haben kürzlich ein dreijähriges Modellprojekt 'Qualitätsmarke-Gemeinsame Familienbegleitung' (Signet 'QM_Anerkennung' liegt anbei) beendet. Zielgruppen sind zum Einen Kinder und Jugendliche, die in Erziehungshilfe-Wohngruppen leben und zum Anderen Fach- und Führungskräfte in der Kinder- und Jugendhilfe. Über Ablauf und Schlussfolgerungen aus dem abgeschlossenen Modellprojekt soll eine 30-seitige Broschüre mit dem Titel 'Hier wächst Mitsprache' Untertitel 'Ein Wegweiser zur Qualitätsmarke' Auskunft geben.
Aufgabenstellung
- Broschüre im DIN A4 - Format,
- Dummy-Text für Projektstruktur und -beteiligte,
- Formschönes und dynamisches Design,
- Platzhalter für eigene Bilder (max. 3 pro Seite),
- die 6 Einrichtungslogos in einer Reihe auf dem Deckblatt vorne (unten),
- Der Broschüreninhalt ist in der PDF 'Kurzvorstellung enthalten',
- Vorgaben zum CD im PDF 'Hauptmanual KWF',
- Das KWF-Signet, wie im Manual beschrieben,
- das ebenfalls hochgeladene Gütesiegel kommt auf das Deckblatt

```html
<!DOCTYPE html>
<html lang="de">
<head>
<meta charset="utf-8">
<title>Hier wächst Mitsprache – Broschüre</title>
<link rel="stylesheet" href="https://fonts.googleapis.com/css2?family=Fira+Sans:wght@400;500;600&family=Merriweather:wght@400;700&display=swap">
<style>
  :root{
    --stage:#e4e4e4;
    --paper:#ffffff;
    --cover-paper:#f2f2f2;
    --brand-blue:#1e62ad;
    --soft-blue:#dbe6f3;
    --ink:#2b2b2b;
    --muted:#6a6a6a;
    --green:#2c9a48;
    --seal-green:#1f6b55;
  }
  *{box-sizing:border-box;margin:0;padding:0}
  html,body{width:1200px;height:675px;overflow:hidden;background:var(--stage)}
  body{position:relative;font-family:"Fira Sans",Arial,sans-serif;color:var(--ink)}
  .page{position:absolute;top:68px;width:382px;height:540px;background:var(--paper);overflow:hidden;box-shadow:0 2px 10px rgba(0,0,0,.12)}
  .page--left{left:24px}
  .page--right{left:406px;border-left:1px solid #e2e2e2}
  .page--cover{left:796px;background:var(--cover-paper)}

  .body-text{font-family:Merriweather,Georgia,serif;font-size:6.2px;line-height:1.55;color:var(--ink)}
  .body-text p+p{margin-top:6px}
  .lead-heading{font-size:8.5px;line-height:1.25;color:var(--brand-blue);font-weight:500;margin-bottom:5px}

  /* left page */
  .story-title{position:absolute;left:28px;top:30px;font-size:24px;font-weight:500;color:var(--brand-blue)}
  .story-sub{position:absolute;left:28px;top:62px;width:320px;font-size:8.5px;line-height:1.3;color:var(--brand-blue)}
  .col{position:absolute;width:152px}
  .col--a{left:28px;top:100px}
  .col--b{left:198px;top:100px}
  .photo{display:block}
  .photo--group{width:152px;height:110px;margin:10px 0;background:linear-gradient(135deg,#c9b9a6,#8a7868 55,#4f5d78)}
  .tips-box{background:var(--soft-blue);border-radius:8px;padding:10px 10px 10px;margin:10px 0}
  .tips-box h3{font-size:11px;font-weight:500;color:var(--green);margin-bottom:6px}
  .tips-box li{list-style:none;position:relative;padding-left:9px;font-family:Merriweather,Georgia,serif;font-size:6px;line-height:1.5;font-weight:700;margin-bottom:5px}
  .tips-box li::before{content:"";position:absolute;left:0;top:2px;border-left:5px solid var(--green);border-top:3px solid transparent;border-bottom:3px solid transparent}
  .folio{position:absolute;left:28px;bottom:18px;font-size:6.5px;color:var(--muted)}
  .folio b{color:var(--brand-blue);font-weight:500;margin-right:4px}

  /* right page */
  .photo--portrait{position:absolute;left:0;top:0;width:382px;height:250px;background:linear-gradient(120deg,#e9e3da 0%,#c7a98e 40%,#6d5443 75%,#3a3a3a 100%)}
  .inset-photo{position:absolute;left:262px;top:212px;width:44px;height:44px;border-radius:50%;border:3px solid var(--green);background:linear-gradient(135deg,#d9b9a0,#8d6e5a)}
  .quote-box{position:absolute;left:238px;top:240px;width:130px;background:var(--soft-blue);border-radius:8px;padding:22px 10px 10px}
  .quote-box .lead-heading{font-size:8px}
  .col--r1{left:28px;top:262px;width:192px}
  .col--r2{left:238px;top:370px;width:130px}

  /* cover */
  .photo--hands{position:absolute;left:0;top:0;width:382px;height:300px;background:linear-gradient(150deg,#6f8fb4 0%,#3c6a9c 45%,#b98f77 60%,#2e5689 100%)}
  .seal{position:absolute;left:52px;top:40px}
  .cover-title{position:absolute;left:30px;top:338px;width:330px;font-size:21px;line-height:1.3;font-weight:600;color:var(--brand-blue)}
  .partner-row{position:absolute;left:30px;right:22px;top:448px;display:flex;align-items:flex-start;gap:12px}
  .carrier{display:flex;gap:6px;align-items:flex-start}
  .carrier-mark{width:22px;height:22px;background:var(--brand-blue)}
  .carrier-name{font-size:10px;font-weight:500;color:var(--brand-blue);line-height:1.1}
  .carrier-name small{display:block;font-size:5.5px;font-weight:400;color:var(--muted);margin-top:2px}
  .partners{display:grid;grid-template-columns:repeat(3,1fr);gap:8px 8px;flex:1}
  .partner{font-size:5.4px;line-height:1.25;color:var(--ink);font-weight:500}
</style>
</head>
<body>

<section class="page page--left">
  <h1 class="story-title">Erfolgsstory</h1>
  <p class="story-sub">Blindtext steht hier Best Practise – Vorstellung vor Ort, z.B. Selbstportrait/ Rollenbeschreibung eines Gruppensprechers</p>

  <div class="col col--a">
    <h2 class="lead-heading">Reprovi deliciaiam sant eum nus, sum. officia aut ipsapis</h2>
    <div class="body-text">
      <p>Hier erzählt ein Gruppensprecher, wie Beteiligung in seiner Wohngruppe gelebt wird. Er berichtet von Gruppenabenden, gemeinsamen Regeln und kleinen Erfolgen im Alltag.</p>
      <p>Die Jugendlichen planen Ausflüge selbst, stimmen über Anschaffungen ab und bringen ihre Ideen in die Teamsitzungen ein. So wächst Vertrauen auf beiden Seiten.</p>
    </div>
    <div class="photo photo--group" role="img" aria-label="Foto: Jugendliche sitzen lachend zusammen in ihrer Wohngruppe"></div>
    <div class="body-text">
      <p>Wichtig war allen, dass Entscheidungen nachvollziehbar bleiben. Deshalb gibt es eine Wand mit Protokollen, die jeder lesen und ergänzen kann.</p>
    </div>
  </div>

  <div class="col col--b">
    <div class="body-text">
      <p>Anfangs war vieles ungewohnt. Die Fachkräfte mussten lernen, Verantwortung abzugeben, und die Jungen und Mädchen mussten lernen, sie anzunehmen. Nach einigen Monaten lief der Gruppenrat fast von allein und neue Mitglieder wurden von den Älteren eingearbeitet. Heute ist die Runde fester Bestandteil der Woche.</p>
    </div>
    <aside class="tips-box">
      <h3>Good to knows</h3>
      <ul>
        <li>Regeln werden gemeinsam erarbeitet und regelmäßig überprüft.</li>
        <li>Jede Stimme zählt, auch die der Jüngsten in der Gruppe.</li>
        <li>Beschwerden haben einen festen Weg und eine feste Ansprechperson.</li>
        <li>Ergebnisse werden sichtbar gemacht und gemeinsam gefeiert.</li>
      </ul>
    </aside>
    <div class="body-text">
      <p>Der Gruppensprecher wünscht sich, dass andere Einrichtungen den Mut haben, ähnliche Wege zu gehen.</p>
    </div>
  </div>

  <p class="folio"><b>2 |</b>Hier wächst Mitsprache – Ein Wegweiser zur Qualitätsmarke</p>
</section>

<section class="page page--right">
  <div class="photo photo--portrait" role="img" aria-label="Foto: junger Mann zeigt das Victory-Zeichen, mit handgeschriebenem Zitat"></div>
  <div class="inset-photo" role="img" aria-label="Rundes Porträtfoto einer Jugendlichen"></div>
  <aside class="quote-box">
    <h3 class="lead-heading">Acestio et, od mil minus</h3>
    <div class="body-text">
      <p>Kurze Stimme aus der Gruppe: Was mir an der Mitsprache am meisten gefällt, ist das Gefühl, ernst genommen zu werden.</p>
    </div>
  </aside>

  <div class="col col--r1">
    <div class="body-text">
      <p>Nach der ersten Projektphase wurden die Erfahrungen gesammelt und in allen beteiligten Häusern ausgewertet.</p>
    </div>
    <h2 class="lead-heading" style="margin-top:10px">At atquatum eaque doluptatis es maximag nienis et</h2>
    <div class="body-text">
      <p>Die Auswertung zeigte, dass feste Formate wie Gruppenrat und Sprechstunde besonders gut angenommen werden. Wo sie fehlen, sinkt die Beteiligung spürbar.</p>
    </div>
    <h2 class="lead-heading" style="margin-top:10px">Millab ipitatis mo quis aut porepudam, ventis un aliquunt occus.</h2>
    <div class="body-text">
      <p>Für die Zukunft sind Schulungen für neue Mitarbeitende geplant.</p>
    </div>
  </div>

  <div class="col col--r2">
    <div class="body-text">
      <p>Die Ergebnisse fließen in die Leitlinien aller Träger ein und werden jährlich fortgeschrieben.</p>
    </div>
  </div>
</section>

<section class="page page--cover">
  <div class="photo photo--hands" role="img" aria-label="Foto: viele Hände übereinander gestapelt als Zeichen des Zusammenhalts"></div>
  <svg class="seal" width="68" height="68" viewBox="0 0 68 68" role="img" aria-label="Siegel der Qualitätsmarke">
    <circle cx="34" cy="34" r="33" fill="#ffffff"/>
    <circle cx="34" cy="34" r="24" fill="var(--seal-green)"/>
  </svg>

  <h1 class="cover-title">Hier wächst Mitsprache –<br>Ein Wegweiser zur Qualitätsmarke</h1>

  <div class="partner-row">
    <div class="carrier">
      <span class="carrier-mark"></span>
      <p class="carrier-name">KWF<small>Gruppe<br>Küstenwerk<br>für Familien</small></p>
    </div>
    <div class="partners">
      <p class="partner">Arbeitskreis Jugendhilfe Nordufer</p>
      <p class="partner">Jugendhilfe Lindenhof</p>
      <p class="partner">Jugendhilfe Weidenland</p>
      <p class="partner">Kinderhäuser Am Mühlenbach</p>
      <p class="partner">Pädagogische Hilfen Heidekamp</p>
      <p class="partner">Sozialpädagogische Hilfen Birkenau</p>
    </div>
  </div>
</section>

</body>
</html>
```